Portfolio of Country Home designs

I need a ppt presentation to show approximately 12 to 26 home designs that my company has completed, and images of home designs that are available.

Most of the illustrations will be exterior shots, but there will be a few interior details and perhaps a few floorplans as well.

The presentation will have a short introductory text (which I will provide).

The majority of the presentation will be photos or illustrations laid out on a standard page which you will design.

The page design will be very important. We need to show quality, trust, luxury, vacation home lifestyle.

The design of the presentation should be contemporary, modern - but with a very slight "rustic" note since the homes are mostly intended for construction in the countryside of Laurentian Mountain region of Quebec, Canada. Clean, NOT fancy.

The photos and illustrations will be in various sizes and formats (ie: actual photos, renderings or drawings).. therefore the page design will be flexible to accommodate different source images and still make the presentation cohesive and uniform.

My company is Tamsworth Harbour Properties. There are some sample photos and illustrations attached for your reference

My name is Dennis, I look forward to your proposals

```html
<!DOCTYPE html>
<html lang="en">
<head>
<meta charset="utf-8">
<title>Project Title Here – Tamsworth Harbour Properties</title>
<link href="https://fonts.googleapis.com/css2?family=Noto+Serif:wght@400;700&display=swap" rel="stylesheet">
<style>
  :root {
    --forest: #2f6c19;
    --forest-dark: #2a6216;
    --harvest: #f2b64f;
    --paper: #ffffff;
    --ink: #3b3526;
    --photo-sky: #8a9aa8;
    --photo-wood: #6b5a3e;
    --photo-grass: #4f6b2e;
  }
  * { margin: 0; padding: 0; box-sizing: border-box; }
  html, body { width: 1200px; height: 900px; overflow: hidden; background: var(--harvest); }
  .slide {
    position: relative;
    width: 1200px;
    height: 900px;
    overflow: hidden;
    background: var(--harvest);
    font-family: "Noto Serif", Georgia, serif;
  }
  .slide__header-shape { position: absolute; inset: 0; width: 1200px; height: 200px; }
  .slide__title {
    position: absolute;
    left: 66px;
    top: 28px;
    color: var(--paper);
    font-size: 40px;
    font-weight: 400;
    letter-spacing: 0.2px;
  }
  .brand {
    position: absolute;
    right: 14px;
    top: 20px;
    display: flex;
    align-items: center;
    gap: 10px;
  }
  .brand__mark {
    width: 22px;
    height: 22px;
    background: var(--harvest);
  }
  .brand__name {
    width: 140px;
    color: var(--paper);
    font-size: 15px;
    font-weight: 700;
    line-height: 1.2;
    text-transform: uppercase;
    letter-spacing: 0.5px;
  }
  .project {
    position: absolute;
    left: 55px;
    width: 1130px;
    display: flex;
    gap: 33px;
  }
  .project--one { top: 168px; }
  .project--two { top: 391px; }
  .project--three { top: 609px; }
  .project__frame {
    flex: none;
    width: 368px;
    height: 204px;
    padding: 6px;
    background: var(--paper);
    box-shadow: 1px 2px 5px rgba(60, 40, 0, 0.35);
  }
  .project__photo { width: 100%; height: 100%; }
  .project__photo--lodge { background: linear-gradient(180deg, var(--photo-sky) 0%, var(--photo-wood) 45%, var(--photo-grass) 100%); }
  .project__photo--chalet { background: linear-gradient(180deg, #6f7d6a 0%, #9c8a66 45%, #7d7a5a 100%); }
  .project__photo--dusk { background: linear-gradient(180deg, #5d7391 0%, #3d4350 50%, #55585a 100%); }
  .project__text {
    width: 680px;
    margin-top: 12px;
    color: var(--ink);
    font-size: 19.5px;
    line-height: 30.8px;
  }
  .slide__footer {
    position: absolute;
    left: 0;
    bottom: 0;
    width: 1200px;
    height: 63px;
    background: var(--forest);
  }
</style>
</head>
<body>
<main class="slide">
  <svg class="slide__header-shape" viewBox="0 0 1200 200" aria-hidden="true">
    <path d="M0,0 H1200 V112 Q560,60 0,150 Z" fill="var(--forest)"/>
    <path d="M0,150 Q560,60 1200,112" fill="none" stroke="var(--paper)" stroke-width="4"/>
  </svg>

  <h1 class="slide__title">Project Title Here</h1>

  <div class="brand">
    <span class="brand__mark"></span>
    <span class="brand__name">Tamsworth Harbour Properties</span>
  </div>

  <section class="project project--one">
    <div class="project__frame">
      <div class="project__photo project__photo--lodge" role="img" aria-label="Photo of a timber lodge home at dusk with a stone path across the lawn"></div>
    </div>
    <p class="project__text">Lorem ipsum dolor sit Lorem ipsum dolor sit Lorem ipsum dolor sit Lorem ipsum dolor sitLorem ipsum dolor sit Lorem ipsum dolor sit Lorem ipsum dolor sit Lorem ipsum dolor sit Lorem ipsum dolor sit Lorem ipsum dolor sit Lorem ipsum dolor sit Lorem ipsum dolor sitLorem ipsum dolor sit Lorem ipsum dolor sit Lorem ipsum dolor sit Lorem ipsum dolor sit</p>
  </section>

  <section class="project project--two">
    <div class="project__frame">
      <div class="project__photo project__photo--chalet" role="img" aria-label="Rendering of a wooden country chalet with large windows among trees"></div>
    </div>
    <p class="project__text">Lorem ipsum dolor sit Lorem ipsum dolor sit Lorem ipsum dolor sit Lorem ipsum dolor sitLorem ipsum dolor sit Lorem ipsum dolor sit Lorem ipsum dolor sit Lorem ipsum dolor sit Lorem ipsum dolor sit Lorem ipsum dolor sit Lorem ipsum dolor sit Lorem ipsum dolor sitLorem ipsum dolor sit Lorem ipsum dolor sit Lorem ipsum dolor sit Lorem ipsum dolor sit</p>
  </section>

  <section class="project project--three">
    <div class="project__frame">
      <div class="project__photo project__photo--dusk" role="img" aria-label="Rendering of a large gabled country home in evening light with a driveway"></div>
    </div>
    <p class="project__text">Lorem ipsum dolor sit Lorem ipsum dolor sit Lorem ipsum dolor sit Lorem ipsum dolor sitLorem ipsum dolor sit Lorem ipsum dolor sit Lorem ipsum dolor sit Lorem ipsum dolor sit Lorem ipsum dolor sit Lorem ipsum dolor sit Lorem ipsum dolor sit Lorem ipsum dolor sitLorem ipsum dolor sit Lorem ipsum dolor sit Lorem ipsum dolor sit Lorem ipsum dolor sit</p>
  </section>

  <footer class="slide__footer"></footer>
</main>
</body>
</html>
```